Kestrel Roofpower Company need Flier for Bureau of Fuel Planning

We need a 2 page flier for distributing to Military Contractors and Bureau of Fuel Planning. We install residential solar and this will be used for military base housing and other gov. projects on the residential home communities. We need to show how large of a company we are and how we are able to work with the military //gov. projects. Attached is our website and other marketing info for your use. Thanks and good luck!

Target Market(s)

Military and Government Contractors //Bureau of Fuel Planning

Industry/Entity Type

Solar Energy

Requirements
Must have
• Our Why - Statement included

```html
<!DOCTYPE html>
<html lang="en">
<head>
<meta charset="utf-8">
<title>Kestrel Roofpower Company – Solar Flier</title>
<link href="https://fonts.googleapis.com/css2?family=Fira+Sans:ital,wght@0,400;0,500;0,600;0,700;1,600&family=Oswald:wght@600&display=swap" rel="stylesheet">
<style>
:root{
  --stage:#3b3b3b;
  --cream:#fdfbe8;
  --green:#8dc63f;
  --green-dark:#6da52b;
  --orange:#f7941d;
  --blue:#1a97d5;
  --blue-dark:#1580bb;
  --slate:#58595b;
  --ink:#1e1e1e;
  --muted:#5e5e5e;
  --card:#f1f3f5;
  --white:#ffffff;
}
*{box-sizing:border-box;margin:0;padding:0}
html,body{width:1200px;height:809px;overflow:hidden;background:var(--stage)}
body{position:relative;font-family:"Fira Sans",Arial,sans-serif}
.page{position:absolute;overflow:hidden}
.abs{position:absolute}

/* ---------- Page one ---------- */
.page-one{left:30px;top:51px;width:560px;height:722px;background:var(--cream)}
.hero-photo{left:7px;top:7px;width:260px;height:158px;
  background:linear-gradient(90deg,#b5532a 0%,#e08a45 45%,rgba(248,214,150,.6) 75%,rgba(253,251,232,0) 100%)}
.page-one .headline{right:32px;top:28px;font-size:22px;font-weight:600;color:var(--orange);white-space:nowrap}
.tagline{right:32px;top:66px;font-size:12.5px;font-weight:600;color:var(--ink);white-space:nowrap;display:flex;align-items:center;gap:7px}
.dot{display:inline-block;width:9px;height:9px;border-radius:50%;background:var(--orange)}
.page-one .site{right:32px;top:128px;font-size:20px;font-weight:700;color:var(--blue);letter-spacing:.6px}

.intro-band{left:7px;top:165px;width:546px;height:336px;background:var(--green)}
.install{left:27px;top:20px;color:var(--white);font-weight:600;line-height:1.1}
.install .big{font-size:22px;display:block;margin-bottom:8px}
.install .mid{font-size:15.5px}
.install .small{font-size:12px}
.install p{margin-bottom:6px}
.divider{left:222px;top:28px;width:1px;height:160px;background:rgba(255,255,255,.55)}
.why{left:245px;top:24px;width:278px;color:var(--white);font-size:8.2px;line-height:1.32;text-align:justify}
.why p{margin-bottom:9px}

.feature{top:196px;height:128px;background:var(--white);padding:8px 6px}
.feature h3{font-size:13px;font-weight:600;color:var(--blue);line-height:1.2;margin-bottom:6px}
.feature p{font-size:8px;color:var(--muted);line-height:1.35}
.f1{left:27px;width:112px}
.f2{left:154px;width:115px}
.f3{left:282px;width:114px}
.f4{left:406px;width:116px}
.f2 p{width:72px}
.f2 .tag{position:absolute;left:6px;bottom:12px;font-size:8.5px;font-weight:600;color:#38a935}
.f2 .coin{position:absolute;right:8px;top:48px;width:30px;height:30px;border-radius:50%;background:var(--green)}
.feature svg{position:absolute;left:6px;bottom:6px}

.voice-band{left:7px;top:501px;width:546px;height:106px;background:var(--blue)}
.voice-band h2{position:absolute;left:29px;top:10px;font-size:17px;font-style:italic;font-weight:600;color:var(--white)}
.voice-rule{left:218px;top:21px;width:301px;height:3px;background:var(--orange)}
.quote{top:38px;width:152px;color:var(--white);font-size:7.6px;line-height:1.28;text-align:justify}
.quote .who{display:block;text-align:right;font-weight:600;margin-top:4px}
.q1{left:26px}.q2{left:205px}.q3{left:383px}

.roof-photo{top:607px;height:108px}
.r1{left:7px;width:195px;background:linear-gradient(180deg,#b9c9c8 0%,#9e4a36 45%,#c47d5a 70%,#6d9c49 100%)}
.r2{left:206px;width:154px;background:linear-gradient(160deg,#d9d0b8 0%,#3f5f8d 40%,#c8c0a8 75%,#b8b39f 100%)}
.r3{left:363px;width:190px;background:linear-gradient(180deg,#b8c3cf 0%,#9aa6b3 30%,#2e4466 55%,#b0582f 85%,#8c4324 100%)}

/* ---------- Page two ---------- */
.page-two{left:610px;top:50px;width:561px;height:722px;background:var(--white)}
.top-art{left:0;top:0}
.page-two .title{left:27px;top:38px;font-family:"Oswald",Impact,sans-serif;font-weight:600;color:var(--white);font-size:54px;line-height:.93;letter-spacing:.5px}
.audience{left:28px;top:152px;font-size:17.5px;font-weight:600;color:var(--ink);line-height:1.5}
.zero{left:27px;top:212px;font-size:25px;font-weight:600;color:var(--white)}
.page-two .site{left:26px;top:258px;font-size:21px;font-weight:600;color:var(--white);letter-spacing:.6px}
.mission{left:28px;top:293px;width:345px;color:var(--white);font-size:7.6px;line-height:1.3}
.mission p{margin-bottom:6px}
.brand{left:402px;top:300px;width:153px;text-align:center}
.brand .ring{width:62px;height:62px;border-radius:50%;border:6px solid var(--green);margin:0 auto 8px}
.brand .name{font-size:14.5px;font-weight:500;color:var(--blue);line-height:1.1;letter-spacing:.4px}
.sun-band{left:0;top:406px;width:561px;height:39px;background:var(--orange);color:var(--white);font-size:21.5px;font-weight:600;text-align:center;line-height:39px;letter-spacing:.2px}
.easy{left:0;top:472px;width:561px;text-align:center;font-size:21px;font-weight:600;color:#3d3d3d}
.step{top:493px;height:147px;background:var(--card);text-align:center;padding-top:12px}
.step .icon{width:50px;height:50px;border-radius:50%;border:3px solid var(--blue);margin:0 auto 12px;display:flex;align-items:center;justify-content:center;background:var(--white)}
.step.alt .icon{border-color:var(--green)}
.step h3{font-size:12px;font-weight:600;color:var(--blue);line-height:1.2;margin-bottom:7px}
.step p{font-size:8.4px;color:#3d3d3d;line-height:1.35;padding:0 4px}
.s1{left:35px;width:119px}
.s2{left:164px;width:111px}
.s3{left:285px;width:117px}
.s4{left:413px;width:134px}
.arrow{top:515px}
.page-two .tagline{left:0;right:0;top:652px;justify-content:center;font-size:13.5px}
.footer{left:0;top:676px}
.footer-text{top:676px;height:46px;display:flex;align-items:center}
.mail{left:28px;font-size:14px;font-weight:500;color:var(--ink)}
.mail b{font-weight:700}
.quote-call{left:300px;gap:10px;color:var(--white)}
.quote-call i{font-size:12px;font-weight:600}
.quote-call span{font-size:22px;font-weight:600}
</style>
</head>
<body>

<!-- Page one -->
<section class="page page-one">
  <div class="abs hero-photo" role="img" aria-label="Family silhouetted against a sunset sky"></div>
  <h1 class="abs headline">Bringing the Power of the SUN for you</h1>
  <div class="abs tagline">Zero upfront Cost <span class="dot"></span> Lower monthly Energy Costs</div>
  <div class="abs site">www.KestrelRoofpower.com</div>

  <div class="abs intro-band">
    <div class="abs install">
      <span class="big">We install</span>
      <p class="mid">Residential Solar</p>
      <p><span class="small">and this will be used </span><span class="mid">For</span></p>
      <p class="mid">Military base housing</p>
      <p><span class="small">and other </span><span class="mid">govt. projects</span></p>
      <p class="small">on the Residential Home</p>
      <p class="small">Communities.</p>
    </div>
    <div class="abs divider"></div>
    <div class="abs why">
      <p>We are on a mission to empower home owners and businesses to power their lives with better, less expensive, cleaner energy creating a world that is powered by the sun.</p>
      <p>With solar, homeowners are saving money while dramatically lessening the amount of pollution released into the atmosphere. We believe that, together, we can create a planet run by the sun.</p>
      <p>Everyone should have the freedom to choose where they get their energy and be able to control their energy costs. Homeowners across the nation rely on us to provide $0 upfront cost options in upgrading their home to solar energy in a way that saves them money on monthly electrical costs.</p>
      <p>Smart and forward thinking, Solar allows you the ability to lower your energy bills and avoid the costly rate increases.</p>
    </div>

    <div class="abs feature f1">
      <h3>Reduce Energy</h3>
      <p>Protect your organization from rising energy prices.</p>
      <svg width="100" height="62" viewBox="0 0 100 62">
        <rect x="4" y="2" width="54" height="58" fill="#a9b4c2"/>
        <text x="18" y="36" font-size="7" fill="#fff" font-family="Fira Sans">Utility</text>
        <text x="20" y="45" font-size="7" fill="#fff" font-family="Fira Sans">Price</text>
        <polygon points="60,0 98,0 98,14 79,22 60,14" fill="#6aa84f"/>
        <text x="68" y="12" font-size="8" fill="#fff" font-weight="600" font-family="Fira Sans">SAVE</text>
        <rect x="60" y="28" width="38" height="32" fill="#8dc63f"/>
        <text x="66" y="42" font-size="7" fill="#fff" font-family="Fira Sans">SOLAR</text>
        <text x="69" y="51" font-size="7" fill="#fff" font-family="Fira Sans">Price</text>
      </svg>
    </div>
    <div class="abs feature f2">
      <h3>Savings Beyond Solar</h3>
      <p>SunHarbor energy efficiency solutions help you use less energy and save money</p>
      <div class="coin"></div>
      <span class="tag">Energy Efficiency</span>
    </div>
    <div class="abs feature f3">
      <h3>What Will Electricity Cost?</h3>
      <p>SunHarbor makes it easy and affordable to save with solar.</p>
      <svg width="102" height="54" viewBox="0 0 102 54">
        <polygon points="4,40 98,4 98,40" fill="#8dc63f"/>
        <polygon points="4,40 98,28 98,40" fill="#a9b4c2"/>
        <line x1="4" y1="40" x2="98" y2="40" stroke="#555" stroke-width=".8"/>
        <text x="14" y="28" font-size="5" fill="#444" transform="rotate(-17 14 28)" font-family="Fira Sans">Utility Bill Without Solar</text>
        <text x="20" y="38" font-size="5" fill="#fff" font-family="Fira Sans">Utility Bill With Solar</text>
        <text x="2" y="51" font-size="5" fill="#444" font-family="Fira Sans">Year 1</text>
        <text x="36" y="51" font-size="5" fill="#444" font-family="Fira Sans">Year 10</text>
        <text x="80" y="51" font-size="5" fill="#444" font-family="Fira Sans">Year 20</text>
      </svg>
    </div>
    <div class="abs feature f4">
      <h3>Energy Monitoring</h3>
      <p>WattLedger tracks your solar production and electricity consumption</p>
      <svg width="104" height="36" viewBox="0 0 104 36">
        <polygon points="0,26 14,16 26,22 40,12 54,20 70,10 84,18 104,12 104,28 0,28" fill="#c9c9c9"/>
        <g fill="#3aa645">
          <rect x="40" y="18" width="3" height="10"/><rect x="45" y="12" width="3" height="16"/>
          <rect x="50" y="7" width="3" height="21"/><rect x="55" y="4" width="3" height="24"/>
          <rect x="60" y="4" width="3" height="24"/><rect x="65" y="7" width="3" height="21"/>
          <rect x="70" y="12" width="3" height="16"/><rect x="75" y="18" width="3" height="10"/>
        </g>
        <line x1="0" y1="28" x2="104" y2="28" stroke="#999" stroke-width=".8"/>
      </svg>
    </div>
  </div>

  <div class="abs voice-band">
    <h2>What People are saying...</h2>
    <div class="abs voice-rule"></div>
    <p class="abs quote q1">“My husband and I decided to go solar after 3 of our neighbors did. After having it I don’t know why we waited so long!<span class="who">Renee P.</span></p>
    <p class="abs quote q2">“I had met with a few different companies and didn’t care for their options. Our team had an option we liked and we went for it! Its been working great for us.<span class="who">Owen and Clara M.</span></p>
    <p class="abs quote q3">“We were a bit nervous to go solar.. after our consultation with Marcus it was very easy to see that solar was our best option. Now we are saving tons on our electric bill! Thanks !<span class="who">Gary and Linda F.</span></p>
  </div>

  <div class="abs roof-photo r1" role="img" aria-label="Brick house with solar panels on a red tile roof"></div>
  <div class="abs roof-photo r2" role="img" aria-label="Aerial view of a home with a rooftop solar array"></div>
  <div class="abs roof-photo r3" role="img" aria-label="Tiled roof with solar panels and wind turbines behind"></div>
</section>

<!-- Page two -->
<section class="page page-two">
  <svg class="abs top-art" width="561" height="406" viewBox="0 0 561 406">
    <defs>
      <linearGradient id="sky" x1="0" y1="0" x2="1" y2="1">
        <stop offset="0" stop-color="#cfe6f6"/>
        <stop offset=".5" stop-color="#6aa6dc"/>
        <stop offset="1" stop-color="#3f77b6"/>
      </linearGradient>
    </defs>
    <rect x="0" y="0" width="561" height="290" fill="url(#sky)" role="img" aria-label="Blue house with solar panels on its roof under a clear sky"/>
    <polygon points="0,0 176,0 350,270 0,270" fill="var(--green)"/>
    <polygon points="176,0 214,0 392,270 350,270" fill="var(--orange)"/>
    <polygon points="0,254 370,254 370,286 0,286" fill="var(--blue)"/>
    <polygon points="0,286 394,286 382,406 0,406" fill="var(--slate)"/>
    <polygon points="396,270 410,270 396,406 382,406" fill="var(--blue)"/>
    <polygon points="410,270 561,270 561,406 396,406" fill="var(--white)"/>
  </svg>

  <h1 class="abs title">SOLAR<br>ENERGY</h1>
  <div class="abs audience">For Military base Housing<br>and other Govt. Projects</div>
  <div class="abs zero">$0 Upfront Cost</div>
  <div class="abs site">KestrelRoofpower.com</div>

  <div class="abs mission">
    <p>We are on a mission to empower home owners and businesses to power their lives with better, less expensive, cleaner energy creating a world that is powered by the sun. With solar, homeowners are saving money while dramatically lessening the amount of pollution released into the atmosphere. We believe that, together, we can create a planet run by the sun.</p>
    <p>Everyone should have the freedom to choose where they get their energy and be able to control their energy costs. Homeowners across the nation rely on us to provide $0 upfront cost options in upgrading their home to solar energy in a way that saves them money on monthly electrical costs. Smart and forward thinking, Solar allows you the ability to lower your energy bills and avoid the costly rate increases.</p>
  </div>

  <div class="abs brand">
    <div class="ring"></div>
    <div class="name">KESTREL ROOFPOWER<br>COMPANY</div>
  </div>

  <div class="abs sun-band">BRINGING THE POWER OF THE SUN FOR YOU</div>
  <h2 class="abs easy">WE MAKE IT EASY</h2>

  <div class="abs step s1">
    <div class="icon"><svg width="26" height="22" viewBox="0 0 26 22"><rect x="1" y="1" width="24" height="15" rx="1" fill="none" stroke="#1a97d5" stroke-width="2"/><line x1="9" y1="21" x2="17" y2="21" stroke="#1a97d5" stroke-width="2"/><line x1="5" y1="6" x2="13" y2="6" stroke="#8dc63f" stroke-width="2"/><line x1="5" y1="10" x2="19" y2="10" stroke="#8dc63f" stroke-width="2"/></svg></div>
    <h3>Speak to a solar consultant</h3>
    <p>Meet with one of our energy consultants to review your solar options.</p>
  </div>
  <div class="abs step s2">
    <div class="icon"><svg width="28" height="24" viewBox="0 0 28 24"><polygon points="4,2 26,2 22,16 2,16" fill="none" stroke="#1a97d5" stroke-width="2"/><line x1="9" y1="2" x2="7" y2="16" stroke="#1a97d5" stroke-width="1.2"/><line x1="15" y1="2" x2="13" y2="16" stroke="#1a97d5" stroke-width="1.2"/><line x1="21" y1="2" x2="18" y2="16" stroke="#1a97d5" stroke-width="1.2"/><line x1="3" y1="9" x2="24" y2="9" stroke="#1a97d5" stroke-width="1.2"/><line x1="13" y1="16" x2="13" y2="23" stroke="#8dc63f" stroke-width="2"/></svg></div>
    <h3>We’ll design your solar panel system</h3>
    <p>We’ll finalize the details for tip top accuracy.</p>
  </div>
  <div class="abs step s3 alt">
    <div class="icon"><svg width="24" height="24" viewBox="0 0 24 24"><rect x="2" y="2" width="14" height="18" fill="none" stroke="#1a97d5" stroke-width="2"/><circle cx="16" cy="16" r="6" fill="#fff" stroke="#8dc63f" stroke-width="2"/><polyline points="16,13 16,16 18,17" fill="none" stroke="#8dc63f" stroke-width="1.5"/></svg></div>
    <h3>Schedule your<br>1 day install</h3>
    <p>Let us do the heavy lifting as you watch your home upgrade to solar.</p>
  </div>
  <div class="abs step s4 alt">
    <div class="icon"><svg width="24" height="26" viewBox="0 0 24 26"><circle cx="12" cy="11" r="6" fill="none" stroke="#8dc63f" stroke-width="2"/><rect x="9" y="18" width="6" height="5" fill="#8dc63f"/><line x1="12" y1="0" x2="12" y2="3" stroke="#8dc63f" stroke-width="1.5"/><line x1="2" y1="11" x2="4" y2="11" stroke="#8dc63f" stroke-width="1.5"/><line x1="20" y1="11" x2="22" y2="11" stroke="#8dc63f" stroke-width="1.5"/></svg></div>
    <h3>Start saving on your electricity bill</h3>
    <p>Watch your electric bill lower and your energy savings build for year to come.</p>
  </div>

  <svg class="abs arrow" style="left:134px" width="50" height="14" viewBox="0 0 50 14"><path d="M2,8 Q25,16 46,4" fill="none" stroke="#9a9a9a" stroke-dasharray="2 2"/><polyline points="41,3 46,4 44,9" fill="none" stroke="#9a9a9a"/></svg>
  <svg class="abs arrow" style="left:258px" width="50" height="14" viewBox="0 0 50 14"><path d="M2,8 Q25,-2 46,10" fill="none" stroke="#9a9a9a" stroke-dasharray="2 2"/><polyline points="41,10 46,10 45,5" fill="none" stroke="#9a9a9a"/></svg>
  <svg class="abs arrow" style="left:384px" width="50" height="14" viewBox="0 0 50 14"><path d="M2,8 Q25,16 46,4" fill="none" stroke="#9a9a9a" stroke-dasharray="2 2"/><polyline points="41,3 46,4 44,9" fill="none" stroke="#9a9a9a"/></svg>

  <div class="abs tagline">Zero upfront Cost <span class="dot"></span> Lower monthly Energy Costs</div>

  <svg class="abs footer" width="561" height="46" viewBox="0 0 561 46">
    <polygon points="0,0 296,0 278,46 0,46" fill="var(--green)"/>
    <polygon points="296,0 561,0 561,46 278,46" fill="var(--blue)"/>
  </svg>
  <div class="abs footer-text mail">email:&nbsp;<b>info@KestrelRoofpower.com</b></div>
  <div class="abs footer-text quote-call"><i>Get a free quote</i><span>(800) 555-0147</span></div>
</section>

</body>
</html>
```